Marks of Dunmore business card design

I need a clean, professional looking design using the attached logo with a bright green/ gray/dark gray/black colors. Maybe even an orange accent if it looks good. I am open to slight changes in the logo if needed. Details below on the info on what should be on the cards. We are a sign company in Ft. Lauderdale FL that specializes in yacht lettering on multi million dollar yachts.

Target Market(s)

marine industry, yachts

Industry/Entity Type

Business

Colors
9bcb3c
000000
606060
f37122

Requirements
Must have
• address: 4837 W. Tallow Rd.
• Coral Haven, FL 33412
• Phone: 954-518-4062
• email/website: marksofdunmore@postvane.com MarksofDunmore.com
Nice to have
• I would like it very clean and simple but professional looking. Nice layout and would prefer a darker background. Orange highlight only if it works.
Should not have
• Nothing fancy.

```html
<!DOCTYPE html>
<html lang="en">
<head>
<meta charset="utf-8">
<title>Marks of Dunmore Business Card</title>
<link href="https://fonts.googleapis.com/css2?family=Roboto:wght@400;700&display=swap" rel="stylesheet">
<style>
  :root {
    --bg: #e9e9e6;
    --card-dark: #1d1e1f;
    --card-green: #0f9a45;
    --brand-green: #12a049;
    --text-light: #e6e6e6;
    --divider: #8a8a8a;
  }
  html, body {
    margin: 0;
    padding: 0;
    width: 1200px;
    height: 950px;
    overflow: hidden;
    background: var(--bg);
    font-family: "Roboto", Arial, sans-serif;
  }
  .sheet {
    position: relative;
    width: 1200px;
    height: 950px;
  }
  .card {
    position: absolute;
    left: 250px;
    width: 700px;
    height: 400px;
    border-radius: 4px;
    box-shadow: 0 10px 28px rgba(0,0,0,0.22);
  }
  .card-front {
    top: 45px;
    background: var(--card-dark);
  }
  .card-back {
    top: 495px;
    background: var(--card-green);
  }
  .brand-name {
    position: absolute;
    left: 62px;
    top: 124px;
    margin: 0;
    font-weight: 700;
    font-size: 46px;
    color: var(--brand-green);
    line-height: 1;
  }
  .contact-block {
    position: absolute;
    left: 62px;
    top: 212px;
    color: var(--text-light);
  }
  .person-name {
    margin: 0;
    font-size: 17px;
    font-weight: 400;
    color: var(--brand-green);
    text-transform: uppercase;
    letter-spacing: 0.5px;
  }
  .person-role {
    margin: 3px 0 12px;
    font-size: 15px;
    text-transform: uppercase;
  }
  .contact-list {
    list-style: none;
    margin: 0;
    padding: 0;
    font-size: 14px;
    line-height: 22px;
  }
  .contact-list li {
    display: flex;
    align-items: center;
    gap: 9px;
  }
  .contact-icon {
    width: 12px;
    height: 12px;
    fill: var(--brand-green);
    flex: none;
  }
  .divider {
    position: absolute;
    left: 380px;
    top: 214px;
    width: 1px;
    height: 78px;
    background: var(--divider);
  }
  .address {
    position: absolute;
    left: 404px;
    top: 214px;
    margin: 0;
    font-style: normal;
    font-size: 14px;
    line-height: 22px;
    color: var(--text-light);
  }
</style>
</head>
<body>
<main class="sheet">
  <section class="card card-front" aria-label="Business card front">
    <h1 class="brand-name">Marks of Dunmore</h1>

    <div class="contact-block">
      <h2 class="person-name">Evan Calloway</h2>
      <p class="person-role">CEO/Founder</p>
      <ul class="contact-list">
        <li>
          <svg class="contact-icon" viewBox="0 0 24 24" aria-hidden="true"><path d="M6.6 10.8c1.4 2.8 3.8 5.1 6.6 6.6l2.2-2.2c.3-.3.7-.4 1-.2 1.1.4 2.3.6 3.6.6.6 0 1 .4 1 1V20c0 .6-.4 1-1 1C10.6 21 3 13.4 3 4c0-.6.4-1 1-1h3.5c.6 0 1 .4 1 1 0 1.3.2 2.5.6 3.6.1.3 0 .7-.2 1z"/></svg>
          954-518-4062
        </li>
        <li>
          <svg class="contact-icon" viewBox="0 0 24 24" aria-hidden="true"><path d="M2 5h20v14H2z M2 5l10 8 10-8" /></svg>
          marksofdunmore@postvane.com
        </li>
        <li>
          <svg class="contact-icon" viewBox="0 0 24 24" aria-hidden="true"><circle cx="12" cy="12" r="10"/></svg>
          www.MarksofDunmore.com
        </li>
      </ul>
    </div>

    <div class="divider" aria-hidden="true"></div>

    <address class="address">
      4837 W. Tallow Rd.<br>
      Coral Haven, FL 33412
    </address>
  </section>

  <section class="card card-back" aria-label="Business card back"></section>
</main>
</body>
</html>
```